来年3月31日に期限が迫っているインボイス制度について、まだまだ関係ある方にも周知はされていません。
もちろん税務関係なので、税理士さんを始めとして、いろいろな方が、セミナー開催やポルネットとかでも語っていらっしゃいます。
ところが、職種によっては、今更、込み入った話など聞きたくない、面倒だ、聞いてもよく理解できないといった方が多々おられます。
私は、建築関係の経理に携わっており、身近にも、そんな方々を目にしていて危惧している状態です。
これが全国となったら、いったいどれだけの人が、わからないまま期日を迎えてしまうのでしょう。
その中で、とくに今回 ひとり親方にターゲットを絞って、せめて、その方々に向けて、いちからわかるように、しかも語りかけるつもりで書きました。
本文を添付いたしますので、その意向を汲んでいただいた上での電子書籍の表紙デザインをお願いしたいです。
一目で見て、これなら一度読んでみるかと思っていただけるようなものを期待しております。
是非とも、宜しくお願い致します。

```html
<!DOCTYPE html>
<html lang="ja">
<head>
<meta charset="utf-8">
<title>ひとり親方のための いちからわかる インボイス制度</title>
<link href="https://fonts.googleapis.com/css2?family=M+PLUS+Rounded+1c:wght@800;900&family=Noto+Sans+JP:wght@700;900&display=swap" rel="stylesheet">
<style>
  :root {
    --paper: #ffffff;
    --ink: #1b1b1b;
    --brand-blue: #1f6fc4;
    --sky-blue: #3ba6e6;
    --deep-blue: #1d5fae;
    --navy: #1f3157;
    --figure-light: #e9edf2;
    --figure-dark: #b9c2cc;
  }
  * { margin: 0; padding: 0; box-sizing: border-box; }
  html, body { width: 750px; height: 1200px; overflow: hidden; background: var(--paper); }
  .cover {
    position: relative; width: 750px; height: 1200px; overflow: hidden;
    background: var(--paper);
    font-family: "Noto Sans JP", sans-serif;
    color: var(--ink);
  }
  .audience {
    position: absolute; left: 38px; top: 50px;
    font-family: "M PLUS Rounded 1c", sans-serif; font-weight: 900;
    font-size: 72px; line-height: 1.2; white-space: nowrap;
  }
  .audience .dot { position: relative; }
  .audience .dot::before {
    content: ""; position: absolute; left: 50%; top: -10px;
    width: 12px; height: 12px; margin-left: -6px;
    border-radius: 50%; background: var(--ink);
  }
  .lead {
    position: absolute; left: 38px;
    font-family: "M PLUS Rounded 1c", sans-serif; font-weight: 900;
    color: var(--brand-blue); line-height: 1; white-space: nowrap;
    border-bottom: 4px solid var(--brand-blue); padding-bottom: 8px;
  }
  .lead .big { font-size: 112px; }
  .lead .small { font-size: 70px; color: var(--ink); }
  .lead-1 { top: 200px; width: 424px; }
  .lead-2 { top: 345px; width: 424px; }
  .title-block {
    position: absolute; display: flex; flex-direction: column; align-items: center;
    justify-content: space-around;
    font-family: "Noto Sans JP", sans-serif; font-weight: 900; color: #fff;
    line-height: 1;
  }
  .title-block span { display: block; line-height: 1; }
  .title-main { left: 487px; top: 195px; width: 263px; height: 925px; background: var(--sky-blue); font-size: 145px; padding: 10px 0; }
  .title-sub { left: 350px; top: 762px; width: 137px; height: 358px; background: var(--deep-blue); font-size: 112px; padding: 10px 0; }
  .worker-art {
    position: absolute; left: 0; top: 490px; width: 487px; height: 710px;
    background: linear-gradient(180deg, var(--figure-light), var(--figure-dark));
  }
  .accent-band { position: absolute; left: 350px; top: 1120px; width: 400px; height: 80px; background: var(--brand-blue); }
  .author {
    position: absolute; left: 0; top: 1000px; width: 212px; padding: 12px 18px;
    background: var(--navy); color: #fff; font-weight: 700; font-size: 38px; line-height: 1.2;
  }
</style>
</head>
<body>
<main class="cover">
  <div class="worker-art" role="img" aria-label="ヘルメットをかぶり木材を肩に担いで笑顔を見せる作業着姿の職人のイラスト"></div>
  <div class="accent-band"></div>

  <p class="audience"><span class="dot">ひ</span><span class="dot">と</span><span class="dot">り</span><span class="dot">親</span><span class="dot">方</span>のための</p>
  <p class="lead lead-1"><span class="big">いち</span><span class="small">から</span></p>
  <p class="lead lead-2"><span class="big">わかる</span></p>

  <h1 class="title-block title-main" aria-label="インボイス制度"><span>イ</span><span>ン</span><span>ボ</span><span>イ</span><span>ス</span></h1>
  <div class="title-block title-sub" aria-hidden="true"><span>制</span><span>度</span></div>

  <p class="author">著者<br>森川陽子</p>
</main>
</body>
</html>
```